Design refresh of existing HR Application

Talvora is an HR & Payroll processing software, already in use by thousands of people. It is a feature packed, enterprise-grade software that is also simple and user friendly. Visit us at https://talvora.example

Seeking a refresh of the app design/UI.

Key objectives are to make it "sleeker", more professional and polished, whist still retaining functionality. Not intended to be a massive overhaul, but more of reorganization and improvements on design elements.

You may login to our demo account to see the app live.
https://app.talvora.example/login
User: demo@talvora.example
Password: Bex47

Target Market(s)

HR Managers, business administrators/owners and employees.

Industry/Entity Type

Business Software

Number of Pages Required

4 page

Font styles to use
Other font styles liked:
• Lato

Colors
0255a3
3377b5
00a990
33b8a4
f37122
faa54b

Requirements
Must have
• Must retain the current functionality on each page.
Nice to have
• Fine to suggest changes to colors, font sizes, card designs, moving sections around and any other design element changes.

```html
<!DOCTYPE html>
<html lang="en">
<head>
<meta charset="utf-8">
<title>Talvora – Dashboard</title>
<link rel="stylesheet" href="https://fonts.googleapis.com/css2?family=IBM+Plex+Sans:wght@400;500;600;700&display=swap">
<style>
:root{
  --teal:#00a68c;
  --teal-dark:#008f78;
  --orange:#f37122;
  --blue:#2f6fb5;
  --bg:#f4f4f4;
  --panel:#ffffff;
  --soft:#f2f2f2;
  --ink:#222;
  --muted:#666;
  --faint:#aaa;
  --line:#e3e3e3;
}
*{box-sizing:border-box;margin:0;padding:0}
html,body{width:1039px;height:1200px;overflow:hidden}
body{font-family:"IBM Plex Sans",Arial,sans-serif;background:var(--bg);color:var(--ink);position:relative}
.abs{position:absolute}

/* sidebar */
.sidebar{left:0;top:0;width:193px;height:1200px;background:var(--teal)}
.brand{height:99px;display:flex;align-items:center;gap:10px;padding-left:26px;color:#fff;font-weight:500;font-size:26px;letter-spacing:.5px}
.brand-dot{width:22px;height:22px;border:2px solid #fff;border-radius:50%}
.nav{list-style:none}
.nav li{height:45px;display:flex;align-items:center;gap:12px;padding-left:25px;color:#fff;font-size:12px;font-weight:600;letter-spacing:.3px;margin:0 14px 0 0;border-bottom:1px solid rgba(255,255,255,.18);margin-left:12px;padding-left:13px}
.nav li.active{background:#fff;color:var(--teal);margin-left:0;margin-right:0;padding-left:25px;border-left:3px solid var(--orange);border-bottom:none;height:42px}
.nav svg{width:17px;height:17px;flex:none}

/* top bar */
.topbar{left:193px;top:0;width:846px;height:42px;background:#fff;box-shadow:0 1px 3px rgba(0,0,0,.06);display:flex;align-items:center;justify-content:flex-end;gap:14px;padding-right:22px;font-size:9px;font-weight:600;color:#333}
.help{width:21px;height:21px;border:1.5px solid #999;border-radius:50%;display:flex;align-items:center;justify-content:center;color:#999;font-size:12px;font-weight:500}
.user{display:flex;align-items:center;gap:7px;line-height:1.2}
.avatar{border-radius:50%;background:linear-gradient(135deg,#c9a88a,#6a4a3a);flex:none}
.caret{width:8px;height:8px}

/* stat cards */
.stat{top:71px;width:185px;height:65px;background:#fff;border-left:3px solid var(--orange);border-top:1px solid var(--line);border-right:1px solid var(--line);border-bottom:1px solid var(--line);display:flex;align-items:center;gap:12px;padding-left:14px}
.stat svg{width:24px;height:24px;flex:none}
.stat-num{color:var(--orange);font-size:19px;font-weight:600;line-height:1}
.stat-label{font-size:10px;font-weight:500;margin-top:3px;letter-spacing:.2px}

.title{font-size:12px;font-weight:600;letter-spacing:.3px;color:#333}
.panel{background:var(--panel);box-shadow:0 1px 3px rgba(0,0,0,.05)}

/* schedule */
.schedule{left:221px;top:194px;width:587px;height:265px;display:flex}
.agenda{width:254px;border-right:1px solid var(--line);padding:18px 15px}
.agenda-item{background:var(--soft);display:flex;align-items:center;height:63px}
.agenda-date{width:56px;text-align:center;border-right:1px solid #ccc;line-height:1.05;font-size:9px;color:#444}
.agenda-date b{display:block;font-size:19px;font-weight:600;color:#333}
.agenda-text{padding-left:19px;font-size:9px;line-height:1.65;color:#222}
.cal{flex:1}
.cal-head{height:51px;display:flex;align-items:center;justify-content:space-between;padding:0 20px 0 26px;font-size:12px;font-weight:500;border-bottom:1px solid var(--line)}
.cal-arrow{width:16px;height:16px;border-radius:50%;background:var(--teal);display:flex;align-items:center;justify-content:center}
.cal-grid{display:grid;grid-template-columns:repeat(7,1fr);font-size:10px;text-align:center}
.cal-grid span{height:33px;line-height:33px;border-right:1px solid var(--line);border-bottom:1px solid var(--line);color:#333}
.cal-grid span:nth-child(7n){border-right:none}
.cal-grid .dow{height:29px;line-height:29px}
.cal-grid .prev{color:var(--faint)}
.cal-grid .today{background:var(--blue);color:#fff;font-weight:600}
.cal-grid .last{border-bottom:none}

/* time off */
.timeoff{left:826px;top:194px;width:186px;height:265px;padding:18px 14px}
.leave-box{background:var(--soft);height:65px;display:flex;align-items:center;gap:14px;padding-left:16px;margin-bottom:13px}
.leave-box svg{width:22px;height:22px;flex:none}
.leave-name{font-size:10.5px;font-weight:500;color:#222}
.leave-val{display:flex;align-items:center;gap:6px;margin-top:2px}
.leave-val b{color:var(--orange);font-size:18px;font-weight:600}
.tag{background:#bbb;color:#fff;font-size:8px;font-weight:700;padding:1px 4px}
.btn-request{height:33px;background:var(--teal);color:#fff;font-weight:600;font-size:12px;display:flex;align-items:center;justify-content:center;letter-spacing:.5px}

/* tardy */
.tardy{left:222px;top:519px;width:292px;height:267px;padding:4px 8px 0 7px}
.tardy::after{content:"";position:absolute;right:6px;top:5px;width:2px;height:250px;background:#ddd}
.tardy::before{content:"";position:absolute;right:6px;top:5px;width:2px;height:20px;background:var(--teal)}
.tardy-row{display:flex;align-items:center;height:34px;border-bottom:1px solid var(--line);padding-left:6px;padding-right:34px}
.tardy-row:last-child{border-bottom:none}
.tardy-name{flex:1;font-size:10px;padding-left:7px}
.tardy-role{font-size:8.5px;width:100px;text-align:right}
.tardy-val{font-size:8.5px;width:32px;text-align:right}

/* on leave */
.onleave{left:531px;top:519px;width:483px;height:267px;padding:15px 16px}
.filters{display:flex;gap:12px}
.chip{height:22px;border:1px solid #ccc;font-size:8.5px;display:flex;align-items:center;padding:0 8px;background:#fff}
.chip.on{background:var(--orange);border-color:var(--orange);color:#fff;font-weight:600;padding:0 10px}
.leave-card{margin-top:18px;margin-left:2px;width:145px;height:114px;background:var(--soft);text-align:center;padding-top:14px}
.leave-card .avatar{margin:0 auto 6px}
.lc-name{font-size:10px;font-weight:700}
.lc-role{font-size:9px;color:#444;margin-top:1px}
.lc-tag{display:inline-block;background:var(--teal);color:#fff;font-size:7px;font-weight:600;padding:3px 7px;margin-top:6px;letter-spacing:.3px}

/* lists */
.list-head{top:817px;display:flex;align-items:center;justify-content:space-between;width:252px}
.starred{border:1.5px solid var(--teal);color:var(--teal);font-size:8.5px;font-weight:700;height:20px;display:flex;align-items:center;gap:4px;padding:0 6px;letter-spacing:.3px;background:#fff}
.starred svg{width:8px;height:8px}
.feed{top:850px;width:252px;height:269px;padding:4px 9px}
.feed-item{display:flex;gap:12px;padding:15px 0 14px 6px;border-bottom:1px solid var(--line);font-size:10px;line-height:1.38;align-items:center}
.feed-item:last-child{border-bottom:none}
.chev{width:19px;height:19px;border:1px solid #ccc;border-radius:50%;flex:none;display:flex;align-items:center;justify-content:center}
.chev svg{width:6px;height:6px}
.empty{display:flex;align-items:center;justify-content:center;font-size:10px;color:#555}

.footer{top:1158px;left:485px;font-size:10px;display:flex;gap:11px;align-items:center;color:#222}
.footer small{font-size:8.5px}
.build{top:1160px;right:12px;font-size:8px;color:#333}
</style>
</head>
<body>

<aside class="sidebar abs">
  <div class="brand"><span class="brand-dot"></span>Talvora</div>
  <ul class="nav">
    <li class="active"><svg viewBox="0 0 24 24" fill="none" stroke="currentColor" stroke-width="1.6"><path d="M3 11l9-7 9 7v9H3z"/><path d="M10 20v-5h4v5"/></svg>DASHBOARD</li>
    <li><svg viewBox="0 0 24 24" fill="none" stroke="#fff" stroke-width="1.6"><circle cx="12" cy="8" r="4"/><path d="M4 21c1-5 4-7 8-7s7 2 8 7"/></svg>EMPLOYEES</li>
    <li><svg viewBox="0 0 24 24" fill="none" stroke="#fff" stroke-width="1.6"><rect x="3" y="5" width="18" height="16"/><path d="M3 10h18M8 3v4M16 3v4"/></svg>CALENDAR</li>
    <li><svg viewBox="0 0 24 24" fill="none" stroke="#fff" stroke-width="1.6"><circle cx="12" cy="12" r="9"/><circle cx="12" cy="12" r="6"/><path d="M12 8v8"/></svg>EXPENSES</li>
    <li><svg viewBox="0 0 24 24" fill="none" stroke="#fff" stroke-width="1.6"><path d="M5 3h10l4 4v14H5z"/><path d="M8 10h8M8 14h6"/></svg>PAYROLL</li>
    <li><svg viewBox="0 0 24 24" fill="none" stroke="#fff" stroke-width="1.6"><circle cx="13" cy="8" r="5"/><path d="M3 18l5-3h6l5 3"/></svg>LOANS</li>
    <li><svg viewBox="0 0 24 24" fill="none" stroke="#fff" stroke-width="1.6"><path d="M4 20v-5M9 20v-8M14 20v-6M19 20V8M4 11l6-5 4 3 6-5"/></svg>PERFORMANCE</li>
    <li><svg viewBox="0 0 24 24" fill="none" stroke="#fff" stroke-width="1.6"><circle cx="12" cy="12" r="9"/><circle cx="12" cy="12" r="5"/><circle cx="12" cy="12" r="1.5"/></svg>ENGAGEMENT</li>
    <li><svg viewBox="0 0 24 24" fill="none" stroke="#fff" stroke-width="1.6"><rect x="5" y="3" width="14" height="18"/><path d="M8 8h8M8 12h8M8 16h8"/></svg>REPORTS</li>
    <li style="border-bottom:none"><svg viewBox="0 0 24 24" fill="#fff"><path d="M10 2h4l.6 3 2.4 1.3 2.8-1.2 2 3.4-2.3 2v2.9l2.3 2-2 3.4-2.8-1.2L14.6 19 14 22h-4l-.6-3L7 17.7l-2.8 1.2-2-3.4 2.3-2v-2.9l-2.3-2 2-3.4L7 6.3 9.4 5z"/><circle cx="12" cy="12" r="3" fill="#00a68c"/></svg>SETTINGS</li>
  </ul>
</aside>

<header class="topbar abs">
  <div class="help">?</div>
  <span style="display:flex;align-items:center;gap:5px">ENGLISH <svg class="caret" viewBox="0 0 10 10" fill="none" stroke="#333" stroke-width="1.5"><path d="M2 3.5l3 3 3-3"/></svg></span>
  <div class="user" style="margin-left:8px">
    <div class="avatar" role="img" aria-label="Administrator profile photo" style="width:22px;height:22px;border:1.5px solid var(--teal)"></div>
    <div>ADMIN, DEMO<br>HR ADMINISTRATOR</div>
    <svg class="caret" viewBox="0 0 10 10" fill="none" stroke="#333" stroke-width="1.5" style="margin-left:6px"><path d="M2 3.5l3 3 3-3"/></svg>
  </div>
</header>

<div class="stat abs" style="left:222px">
  <svg viewBox="0 0 24 24" fill="none" stroke="#00a68c" stroke-width="1.8"><circle cx="12" cy="12" r="10"/><path d="M12 6v6h-4"/></svg>
  <div><div class="stat-num">12</div><div class="stat-label">EVENT AMENDMENTS</div></div>
</div>
<div class="stat abs" style="left:423px">
  <svg viewBox="0 0 24 24" fill="none" stroke="#00a68c" stroke-width="1.8"><path d="M19 13v8H3V5h8"/><path d="M17 3l4 4-9 9H8v-4z"/></svg>
  <div><div class="stat-num">2</div><div class="stat-label">LEAVE REQUESTS</div></div>
</div>
<div class="stat abs" style="left:623px">
  <svg viewBox="0 0 24 24" fill="none" stroke="#00a68c" stroke-width="1.8"><rect x="2" y="4" width="20" height="18"/><path d="M2 9h20M7 2v4M17 2v4"/><circle cx="12" cy="15" r="3.5"/><path d="M10.5 15l1.2 1.2 2-2"/></svg>
  <div><div class="stat-num">7</div><div class="stat-label">EVENT REQUESTS</div></div>
</div>
<div class="stat abs" style="left:825px">
  <svg viewBox="0 0 24 24" fill="none" stroke="#00a68c" stroke-width="1.8"><path d="M3 2h10v18H3zM6 6h4M6 10h4M6 14h4"/><rect x="14" y="11" width="8" height="11"/><path d="M16 14h4M16 17h1M19 17h1M16 20h1M19 20h1"/></svg>
  <div><div class="stat-num">2</div><div class="stat-label">PAYROLLS PENDING</div></div>
</div>

<h2 class="title abs" style="left:220px;top:165px">MY SCHEDULE</h2>
<h2 class="title abs" style="left:823px;top:165px">MY TIME OFF</h2>

<section class="schedule panel abs">
  <div class="agenda">
    <div class="agenda-item">
      <div class="agenda-date">MAY<b>28</b>THU</div>
      <div class="agenda-text">10:00 WORK (PROJECT A)<br>12:00 BRANCH A</div>
    </div>
  </div>
  <div class="cal">
    <div class="cal-head">
      <span class="cal-arrow"><svg width="8" height="8" viewBox="0 0 10 10" fill="none" stroke="#fff" stroke-width="2"><path d="M6.5 2L3.5 5l3 3"/></svg></span>
      MAY
      <span class="cal-arrow"><svg width="8" height="8" viewBox="0 0 10 10" fill="none" stroke="#fff" stroke-width="2"><path d="M3.5 2l3 3-3 3"/></svg></span>
    </div>
    <div class="cal-grid">
      <span class="dow">M</span><span class="dow">T</span><span class="dow">W</span><span class="dow">T</span><span class="dow">F</span><span class="dow">S</span><span class="dow">S</span>
      <span class="prev">24</span><span class="prev">28</span><span class="prev">29</span><span class="prev">30</span><span>01</span><span>02</span><span>03</span>
      <span>04</span><span>05</span><span>06</span><span>07</span><span>08</span><span>09</span><span>10</span>
      <span>11</span><span>12</span><span>13</span><span>14</span><span>15</span><span>16</span><span>17</span>
      <span>18</span><span>19</span><span>20</span><span>21</span><span>22</span><span>23</span><span>24</span>
      <span class="last">25</span><span class="last">26</span><span class="last">27</span><span class="last today">28</span><span class="last">29</span><span class="last">30</span><span class="last">31</span>
    </div>
  </div>
</section>

<section class="timeoff panel abs">
  <div class="leave-box">
    <svg viewBox="0 0 24 24" fill="none" stroke="#00a68c" stroke-width="2"><path d="M10 4H4v16h6"/><path d="M9 12h9" /><path d="M14 7l6 5-6 5z" fill="#00a68c"/></svg>
    <div><div class="leave-name">ANNUAL LEAVE</div><div class="leave-val"><b>6</b><span class="tag">LEFT</span></div></div>
  </div>
  <div class="leave-box">
    <svg viewBox="0 0 24 24" fill="none" stroke="#00a68c" stroke-width="2"><path d="M12 2l9 3v7c0 5-4 9-9 10-5-1-9-5-9-10V5z"/><path d="M12 8v8M8 12h8" stroke-width="3"/></svg>
    <div><div class="leave-name">SICK DAYS</div><div class="leave-val"><b>1</b><span class="tag">TAKEN</span></div></div>
  </div>
  <div class="btn-request">REQUEST</div>
</section>

<h2 class="title abs" style="left:222px;top:488px">TARDY TODAY</h2>
<h2 class="title abs" style="left:531px;top:488px">WHO'S ON LEAVE TODAY</h2>

<section class="tardy panel abs">
  <div class="tardy-row"><div class="avatar" role="img" aria-label="Employee photo" style="width:23px;height:23px"></div><span class="tardy-name">100, EMPLOYEE</span><span class="tardy-role">HR Administrator</span><span class="tardy-val">8.0</span></div>
  <div class="tardy-row"><div class="avatar" role="img" aria-label="Employee photo" style="width:23px;height:23px"></div><span class="tardy-name">91, EMPLOYEE</span><span class="tardy-role">Factory Worker</span><span class="tardy-val">9.0</span></div>
  <div class="tardy-row"><div class="avatar" role="img" aria-label="Employee photo" style="width:23px;height:23px"></div><span class="tardy-name">EMPLOYEE, DEMO</span><span class="tardy-role">HR Administrator</span><span class="tardy-val">5.9</span></div>
  <div class="tardy-row"><div class="avatar" role="img" aria-label="Employee photo" style="width:23px;height:23px"></div><span class="tardy-name">70, EMPLOYEE</span><span class="tardy-role">Shipping Manager</span><span class="tardy-val">6.5</span></div>
  <div class="tardy-row"><div class="avatar" role="img" aria-label="Employee photo" style="width:23px;height:23px"></div><span class="tardy-name">MANAGER, DEMO</span><span class="tardy-role">HR Manager</span><span class="tardy-val">7.5</span></div>
  <div class="tardy-row"><div class="avatar" role="img" aria-label="Employee photo" style="width:23px;height:23px"></div><span class="tardy-name">19, EMPLOYEE</span><span class="tardy-role">Line Manager</span><span class="tardy-val">2.5</span></div>
  <div class="tardy-row"><div class="avatar" role="img" aria-label="Employee photo" style="width:23px;height:23px"></div><span class="tardy-name">7, EMPLOYEE</span><span class="tardy-role">Accounting Manager</span><span class="tardy-val">3.5</span></div>
</section>

<section class="onleave panel abs">
  <div class="filters">
    <span class="chip on">FILTER</span>
    <span class="chip">SAME DEPARTMENT</span>
    <span class="chip">SAME BRANCH</span>
    <span class="chip">SUBORDINATES</span>
  </div>
  <div class="leave-card">
    <div class="avatar" role="img" aria-label="Employee photo" style="width:27px;height:27px;background:linear-gradient(135deg,#2a8fd0,#1b5d8e)"></div>
    <div class="lc-name">34, EMPLOYEE</div>
    <div class="lc-role">HR Administrator</div>
    <span class="lc-tag">MATERNITY LEAVE</span>
  </div>
</section>

<div class="list-head abs" style="left:223px"><h2 class="title">NOTIFICATIONS</h2><span class="starred"><svg viewBox="0 0 10 10" fill="#00a68c"><path d="M5 0l1.5 3.3 3.5.4-2.6 2.4.7 3.5L5 7.8 1.9 9.6l.7-3.5L0 3.7l3.5-.4z"/></svg>VIEW STARRED</span></div>
<div class="list-head abs" style="left:492px"><h2 class="title">ANNOUNCEMENTS</h2><span class="starred"><svg viewBox="0 0 10 10" fill="#00a68c"><path d="M5 0l1.5 3.3 3.5.4-2.6 2.4.7 3.5L5 7.8 1.9 9.6l.7-3.5L0 3.7l3.5-.4z"/></svg>VIEW STARRED</span></div>
<div class="list-head abs" style="left:762px"><h2 class="title">EMPLOYEE UPDATES</h2><span class="starred"><svg viewBox="0 0 10 10" fill="#00a68c"><path d="M5 0l1.5 3.3 3.5.4-2.6 2.4.7 3.5L5 7.8 1.9 9.6l.7-3.5L0 3.7l3.5-.4z"/></svg>VIEW STARRED</span></div>

<section class="feed panel abs" style="left:223px">
  <div class="feed-item"><span class="chev"><svg viewBox="0 0 6 6" fill="none" stroke="#555" stroke-width="1"><path d="M2 1l2 2-2 2"/></svg></span><span>Marlow, Tessa has remotely checked in for Working on 20/05/2020 02:07</span></div>
  <div class="feed-item"><span class="chev"><svg viewBox="0 0 6 6" fill="none" stroke="#555" stroke-width="1"><path d="M2 1l2 2-2 2"/></svg></span><span>Marlow, Tessa requests amendment on 15 Apr 2020 from 09:00 - 18:00.</span></div>
  <div class="feed-item"><span class="chev"><svg viewBox="0 0 6 6" fill="none" stroke="#555" stroke-width="1"><path d="M2 1l2 2-2 2"/></svg></span><span>Overtime request for Marlow, Tessa - 18 May 2020 at 19:00 | 21:00 Branch A</span></div>
  <div class="feed-item"><span class="chev"><svg viewBox="0 0 6 6" fill="none" stroke="#555" stroke-width="1"><path d="M2 1l2 2-2 2"/></svg></span><span>Marlow, Tessa requests Sick Leave on 19 May 2020.</span></div>
</section>

<section class="feed panel abs" style="left:492px">
  <div class="feed-item"><span class="chev"><svg viewBox="0 0 6 6" fill="none" stroke="#555" stroke-width="1"><path d="M2 1l2 2-2 2"/></svg></span><span>Have a great Hari Lahir Pancasila on 2020-06-01!</span></div>
  <div class="feed-item"><span class="chev"><svg viewBox="0 0 6 6" fill="none" stroke="#555" stroke-width="1"><path d="M2 1l2 2-2 2"/></svg></span><span>Free Friday drinks are available in the on every week until the end of this year. Take the opportunity to get to know more people!</span></div>
</section>

<section class="feed panel empty abs" style="left:762px">There are no Announcements</section>

<footer class="footer abs"><span>Terms</span><span>|</span><span>Privacy</span><span>|</span><small>Copyright © 2020 All Rights Reserved</small></footer>
<span class="build abs">X37</span>

</body>
</html>
```